Management Consultancy needs sharp professional services showcased in a brochure

We are a management consultancy specializing on contract management and conflict avoidance services requiring a professional brochure showcasing our services to prospective clients.

Attached are a selection of existing stationary and the colour scheme.

Further details on our company can be found at www.velto-advisory-partners.com
Updates

Preference is for bi-fold, however, innovative tri-fold will be considered. Added Monday, August 7, 2017

Target Market(s)

Construction companies, consultants, developers, oil and gas service providers, NGO's, SME's.

Industry/Entity Type

Management

Requirements
Must have
• High degree of professionalism with eye catching, sharp detail. No frils.
• Colour scheme as per the attachments
• Font as per attachments - Century Gothic
• Details of our company and services
Nice to have
• Open to ideas, thinking along the lines of a car brochure type design.
• Bi-fold preferred, by trifold accepted if innovative.
Should not have
• Remove reference to the United Arab Emirates.
• No cartoon/clipart photos.

```html
<!DOCTYPE html>
<html lang="en">
<head>
<meta charset="utf-8">
<title>Velto Advisory – Contract and Conflict Advisory Brochure</title>
<link href="https://fonts.googleapis.com/css2?family=Questrial&family=Cinzel:wght@400&display=swap" rel="stylesheet">
<style>
  :root{
    --navy:#1f3350;
    --panel:#2e4a6a;
    --red:#b3262f;
    --ink:#2a2a2a;
    --paper:#ffffff;
    --bg:#e9e9e9;
    --title-bg:#eef0f4;
  }
  *{box-sizing:border-box;margin:0;padding:0}
  html,body{width:765px;height:1200px;overflow:hidden;background:var(--bg)}
  body{font-family:"Questrial","Century Gothic",sans-serif;color:var(--ink);position:relative}
  .sheet{position:absolute;left:20px;width:725px;background:var(--paper);overflow:hidden;box-shadow:0 2px 6px rgba(0,0,0,.18)}
  .sheet::after{content:"";position:absolute;left:0;right:0;bottom:0;height:6px;background:var(--panel)}
  .cover{top:22px;height:562px}
  .inside{top:620px;height:557px}

  /* cover */
  .cover-photo{position:absolute;left:0;top:0;width:725px;height:424px;
    background:linear-gradient(180deg,#f6f4ea 0%,#e3e4e8 18%,#6b6f9a 45%,#4a4470 55%,#b7c3d6 72%,#eef0f3 100%)}
  .cover-photo .pale{position:absolute;right:0;top:0;width:242px;height:100%;background:rgba(255,255,255,.35)}
  .cover-band{position:absolute;left:0;top:424px;width:725px;height:132px;display:flex}
  .contact{width:241px;text-align:center;padding-top:28px;font-size:11px;line-height:15px;color:#555}
  .contact .name{font-family:"Cinzel",serif;font-size:14px;color:var(--navy);margin-bottom:9px;letter-spacing:.5px}
  .contact b{color:var(--navy)}
  .title{width:242px;background:var(--title-bg);text-align:center;font-family:"Cinzel",serif;font-size:19px;line-height:25px;color:var(--navy);padding-top:26px;letter-spacing:.5px}
  .brand{flex:1;display:flex;align-items:center;justify-content:center;font-family:"Cinzel",serif;font-size:22px;color:var(--navy);padding-top:30px}

  /* inside */
  .col{position:absolute;width:208px;font-size:8px;line-height:10.7px;letter-spacing:.1px;text-align:justify}
  .col.c1{left:19px;top:20px}
  .col.c2{left:263px;top:20px}
  .col.c3{left:497px;top:345px;width:214px}
  .panel{position:absolute;left:483px;top:0;width:242px;height:327px;background:var(--panel);color:#fff;padding:20px 14px 0 14px;font-size:8px;line-height:10.7px;letter-spacing:.1px;text-align:justify}
  h2{font-size:16px;font-weight:400;color:var(--navy);letter-spacing:.3px;margin-bottom:10px;font-family:"Questrial",sans-serif;-webkit-text-stroke:.3px var(--navy)}
  .panel h2{color:#fff;-webkit-text-stroke:.3px #fff}
  h3{font-size:9.4px;line-height:11.5px;font-weight:400;color:var(--red);margin:9px 0 5px;text-align:left;-webkit-text-stroke:.25px var(--red)}
  .c3 h3:first-child{margin-top:0}
  p{margin-bottom:4px}
  .panel p{margin-bottom:10px}
  .panel .web{font-size:10.5px;margin-top:6px}
</style>
</head>
<body>

<section class="sheet cover">
  <div class="cover-photo" role="img" aria-label="Photograph of business people in silhouette around a meeting table, reflected over a city skyline">
    <div class="pale"></div>
  </div>
  <div class="cover-band">
    <div class="contact">
      <div class="name">VELTO ADVISORY</div>
      Velto Advisory Limited<br>
      <b>E:</b> mhale@velto-advisory-partners.com<br>
      www.<b>velto-advisory-partners</b>.com
    </div>
    <div class="title">THE CONTRACT<br>AND CONFLICT<br>ADVISORY</div>
    <div class="brand">VELTO ADVISORY</div>
  </div>
</section>

<section class="sheet inside">
  <div class="col c1">
    <h2>CONFLICT ADVISORY</h2>
    <p>Every conflict has the ability to be settled, it is on this premise we deliver effective solutions to contractual and commercial disputes with the aim of preserving the relationships and strengthening the parties for the future ahead.</p>
    <h3>Restoration and Mediation Services</h3>
    <p>Providing advocacy in the field of general commercial and contract issues, real estate, construction (property, civil engineering and vessel - ship and rig) and oilfield services (including aviation, chartering, medical services and purchase).</p>
    <p>Providing effective restoration methods, achieving a mutually acceptable outcome in all phases of the conflict cycle, ensuring that parties leave stronger, more committed and accountable for the progress of the transaction and relationship.</p>
    <h3>Shuttle Diplomacy and In Persona Intermediary Services</h3>
    <p>Providing presence in disputes and processes where parties are:</p>
    <p>(a) unable to attend or<br>(b) unwilling to attend.</p>
    <p>Additionally providing a neutral platform for documentation submission review and filing, aiding vetting and response in shuttle diplomacy.</p>
    <h3>Negotiation Support Services</h3>
    <p>Ensuring success in negotiation, we aim to provide direction in negotiation in the early stages of conflict in order to avert escalation and to reduce conflict aftermath.</p>
    <p>Through assessment of relationship, perception and conflict strategy we ensure adequate negotiation preparation and guidance with the increased outcome of a win win for all parties.</p>
    <h3>Workplace / Corporate Mediation Services</h3>
    <p>Providing effective resolution to workplace misunderstandings, personality conflicts, co-operation and opinion differences, with the objective of increasing workplace performance, and reducing management and HR resource displacement.</p>
  </div>

  <div class="col c2">
    <h2>CONTRACT ADVISORY</h2>
    <p>Effective contract management delivered through our Contract Advisory ensures that the contract is as effective as it can be. Through review, planning and effective application, we ensure that contractual obligations are maintained and risks are mitigated through the full contract life cycle providing the optimum contractual engagement.</p>
    <h3>Contract Troubleshooting</h3>
    <p>Contract Troubleshooting including drafting and interpretation assistance via our "Second Set" protocol.</p>
    <p>Providing secondary review, analysis and interpretation with reporting on application of clauses including layman dissection aiding the deconstruction of terms to reveal the true meaning and implications.</p>
    <p>Contract Workshops with key stakeholders enabling a harmonised understanding of contractual obligations enabling clear procedure establishment.</p>
    <h3>Tender Review &amp; Bid Support</h3>
    <p>Guidance in tender review both recieved and issued</p>
    <p>RFQ and RFP drafting and review.</p>
    <h3>Contracts Audit Services &amp;<br>Performance Management</h3>
    <p>Audit of contractual mechanisms, compliance and corrective reviews on deficiencies.</p>
    <p>Advisory and guidance for corrective measures including performance management and establishment and monitoring of Key performance Indicators ("KPI's").</p>
    <p>Contract harmonisation and benchmarking.</p>
    <p>Post contract maintenance and administration guidance and contract management planning. Third party contract audit including Project Management Consultancy ("PMC")/ Project Management Team ("PMT") process review for major and minor projects.</p>
    <h3>Contract Fraud Investigation</h3>
    <p>Advisory of contract practices which are susceptible to fraudulent activity and investigation of key areas where fraud is suspected.</p>
  </div>

  <div class="panel">
    <h2>OUR SERVICES</h2>
    <p>Every contract has at least two parties; every party has a goal, and every goal matters. Each party must work in equilibrium as a contractual partnership or alliance, it is on this premise we aim to deliver truly mutual agreements, maintaining the contract integrity from inception through the contract life, and where we are not party to the original agreement, we provide effective solutions to contractual conflict via our unique mediation methodology at all positions of the conflict cycle and aim to enhance all aspects of contract performance by effective audit and management.</p>
    <p>We believe that a proactive approach to contract management creates transparency and trust, and maintains relationships and builds on them for the future whilst cultivating significant value to your business transactions and addressing real and relevant issues, providing and implementing effective solutions. We believe that avoidance of contractual conflict and timely resolution on escalation is paramount in the effectiveness of any agreement.</p>
    <p class="web">www.velto-advisory-partners.com</p>
  </div>

  <div class="col c3">
    <h3>Strategic Review &amp; Contract Risk Assessment</h3>
    <p>Advisory of current contract application suitability.</p>
    <p>Steering guidance and contract assessment advisory</p>
    <p>Contractual risk and optimization assessments.</p>
    <p>Development of internal contract management and administration policy and procedure.</p>
    <p>Contract management planning – Advisory at all phases of the contract Life Cycle ("CLC").</p>
    <h3>Temporary Placement Contract<br>Management Solutions</h3>
    <p>Provision of fixed term temporary contract management and contracts administration professionals into your organisation to provide immediate on hand contracts management solutions.</p>
  </div>
</section>

</body>
</html>
```